Flyer Design for Business: "Velvet Dune"

My Business name is "VELVET DUNE"

Laser Hair Removal
Non invasive and pain free
Look amazing and feel confident with a Hair Free body
Now is the time to start don't delay
1 treatment a month will ensure you are bikini hot for the summer months
Take full advantage of our OPENING SPECIALS of 30%-40% savings
Part payments available

CELLULITE & FAT REDUCTION
Now you too can look amazing without invasive surgery, downtime or discomfort
Lorna Pettigrew & Beatrix Holloway are avid recipients of this treatment.
Effective on all skin types and delivers fast measurable results for:
Helping mums regain their pre-baby figures
Losing the love handles (but keeping the love)
Stretch mark reduction
Skin tightening
Cellulite busting on Arms, tummy, thighs.
Man boob reduction.
Latest technology:
Bi Polar radio frequency (RF)
infrared light
negative pressure (Vacuum)
Tissue manipulation through roller mechanical massage.
50% saving Call now

PDT LED REJUVENATION LIGHT THERAPY
KOTR Researchers found:
Fibroblast and muscles grew 5 times faster, stimulates
reconstruction of collagenous fibres of the dermis
These findings and more assist with:
Remove freckles, sunburn pigmentation,
Cures acne and hair follicle inflammation
Anti aging skin tightening
Reduces pore size
Improve the skin texture
Improves circulation
Red light : reduces pore size, softens skin wrinkles,reduces acne
Blue light: Kills the acne bacillus to eliminate acne, inhibit inflammation
Yellow light: Skin tightening, whitening and softens skin wrinkles
Purple light: combination of red & blue lights treats acne scars
Orange light increases cell energy and accelerates metabolism
$55 Saving and relax under the lights.

Who can resist a soothing Hot stone massage therapy after:
A hard stressful day at work
Aches and muscular pain

Pick anything from this info with a couple of nice images.

Target Market(s)

Females & males Sports minded people cyclists

Industry/Entity Type

Beauty Salon

Colors
00a990
e34197

Requirements
Must have
• a couple of images and
Nice to have
• Pink and bluey green like my business card

```html
<!DOCTYPE html>
<html lang="en">
<head>
<meta charset="utf-8">
<title>Velvet Dune – Opening Specials Flyer</title>
<link rel="stylesheet" href="https://fonts.googleapis.com/css2?family=Caveat:wght@500&display=swap">
<style>
  :root {
    --bg-mint: #b3dcc0;
    --ink: #111111;
    --brand-pink: #e8237f;
    --font-hand: "Caveat", cursive;
  }
  html, body {
    margin: 0;
    padding: 0;
    overflow: hidden;
    background: var(--bg-mint);
  }
  .flyer {
    position: relative;
    width: 848px;
    height: 1200px;
    background: var(--bg-mint);
    color: var(--ink);
    font-family: var(--font-hand);
    font-weight: 500;
    overflow: hidden;
  }
  .brand {
    position: absolute;
    top: 140px;
    left: 0;
    width: 100%;
    display: flex;
    justify-content: center;
    align-items: center;
    gap: 22px;
  }
  .brand-dot {
    width: 54px;
    height: 54px;
    border-radius: 50%;
    background: var(--brand-pink);
  }
  .brand-name {
    margin: 0;
    font-size: 84px;
    font-weight: 500;
    line-height: 1;
  }
  .tagline {
    position: absolute;
    top: 446px;
    left: 0;
    width: 100%;
    text-align: center;
    font-size: 32px;
    line-height: 59px;
    margin: 0;
  }
  .offer {
    position: absolute;
    left: 0;
    width: 100%;
    text-align: center;
    margin: 0;
    font-size: 70px;
    line-height: 1;
    letter-spacing: 1px;
  }
  .offer-title { top: 680px; }
  .offer-discount { top: 808px; }
  .offer-payments { top: 900px; left: -38px; }
  .offer-available { top: 1000px; left: 10px; }
</style>
</head>
<body>
  <main class="flyer">
    <header class="brand">
      <span class="brand-dot" aria-hidden="true"></span>
      <h1 class="brand-name">Velvet Dune</h1>
    </header>

    <p class="tagline">
      Look amazing and feel confident with a hair free body<br>
      Laser Hair Removal<br>
      Non invasive and Pain Free
    </p>

    <h2 class="offer offer-title">OPENING SPECIALS</h2>
    <p class="offer offer-discount">30 to 40% off</p>
    <p class="offer offer-payments">PART PAYMENTS</p>
    <p class="offer offer-available">AVAILABLE</p>
  </main>
</body>
</html>
```